Meadowline Lawncare by RT

Design a eye catching EDDM postcard for Lawn Care business... 6.5" x 8" EDDM Postcards with required bleed points

There are a few EDDM rules to follow which are.

1. Be sure to add your Postal Indicia it needs to read
“PRST STD ECRWSS U.S. POSTAGE PAID EDDM RETAIL”
in the top right area of your EDDM Flyer Postcard

2. The address area also needs to be filled in with
“****ECRWSS**** Local Postal Customer”

3. Both of these items need to be present on the same side for example both on the back of your EDDM mailer.
Please see the image on the side here for a visual description on how to set up your EDDM mailer correctly. (Attached Sample Template)

Target Market(s)

Home Owners that has a Lawn Care need

Industry/Entity Type

Lawn Care

Font styles to use
Serif

Colors

Designer to choose colors to be used in the design.

Requirements
Must have
• A beautiful background that capture the homeowner eyes when they open their mailbox and see this small card.
• My number: 409-555-0173
• My Name & Email: Dorian Pelham - dopeturfworks@mailcrest.net

```html
<!DOCTYPE html>
<html lang="en">
<head>
<meta charset="utf-8">
<title>Meadowline Lawncare – EDDM Postcard</title>
<link rel="stylesheet" href="https://fonts.googleapis.com/css2?family=Archivo+Black&family=Archivo:wght@800&family=Oswald:wght@700&family=Arimo:wght@400;700&display=swap">
<style>
  :root{
    --green-light:#b9e872;
    --green-mid:#6cc11e;
    --green-deep:#3f9a10;
    --white:#ffffff;
    --yellow:#f8ee1a;
    --burst-core:#fff35a;
    --burst-edge:#f5b800;
    --red:#e0141c;
    --blue:#1530e8;
    --ink:#111111;
    --card-a:#1a3a9c;
    --card-b:#d8261c;
    --card-c:#2c7ad6;
    --card-d:#f07a12;
  }
  *{margin:0;padding:0;box-sizing:border-box}
  html,body{width:1200px;height:975px;overflow:hidden;background:var(--white)}
  .postcard{position:relative;width:1200px;height:975px;background:var(--white);overflow:hidden;font-family:"Arimo",Arial,sans-serif}

  .lawn-band{position:absolute;left:0;top:0;width:1200px;height:586px;
    background:linear-gradient(180deg,var(--green-light) 0%,var(--green-mid) 45%,var(--green-deep) 100%)}
  .lawn-band::after{content:"";position:absolute;inset:0;
    background:linear-gradient(90deg,rgba(255,255,255,.25) 0%,rgba(255,255,255,0) 55%,rgba(0,60,0,.15) 100%)}

  .headline{position:absolute;left:28px;top:47px;font-family:"Archivo Black",Arial,sans-serif;
    font-size:43px;letter-spacing:.5px;color:var(--white);text-shadow:2px 3px 4px rgba(0,0,0,.45);white-space:nowrap}

  .photo{position:absolute;border:5px solid var(--white);box-shadow:0 2px 6px rgba(0,0,0,.3)}
  .photo--front{left:29px;top:120px;width:478px;height:296px;
    background:linear-gradient(180deg,#c9c4b8 0%,#a9a79a 35%,#7b5a3a 58%,#3d8c1c 75%,#2f7a14 100%)}
  .photo--backyard{left:528px;top:122px;width:467px;height:289px;
    background:linear-gradient(90deg,#111 0 5%,transparent 5% 95%,#111 95%),
               linear-gradient(180deg,#dfe6ea 0%,#b48a5e 35%,#4f9a25 60%,#3c8418 100%)}

  .indicia{position:absolute;left:1018px;top:38px;width:143px;height:142px;background:var(--white);
    border:2px solid var(--ink);text-align:center;font-size:17px;line-height:20px;color:var(--ink);padding-top:16px}
  .indicia b{font-weight:700}

  .perks{position:absolute;left:72px;top:450px;width:720px;list-style:none;display:grid;
    grid-template-columns:356px 350px;row-gap:12px}
  .perk{display:flex;align-items:center;gap:10px;font-family:"Archivo Black",Arial,sans-serif;
    font-size:29px;line-height:32px;color:var(--yellow);text-shadow:1px 2px 3px rgba(0,0,0,.45);white-space:nowrap}
  .perk svg{width:28px;height:28px;flex:none}

  .burst{position:absolute;left:850px;top:355px;width:300px;height:300px}
  .burst-text{position:absolute;left:850px;top:355px;width:300px;height:300px;transform:rotate(8deg);
    font-family:"Oswald",Impact,sans-serif;color:var(--red);text-align:center}
  .burst-text .big{position:absolute;left:0;width:300px;font-size:46px;line-height:50px}
  .burst-text .l1{top:78px}
  .burst-text .l2{top:128px}
  .burst-text .small{position:absolute;left:0;top:186px;width:300px;font-size:30px;line-height:34px}

  .contact{position:absolute;left:0;top:625px;width:800px;color:var(--blue);text-align:center}
  .contact .phone{width:820px;font-family:"Archivo",Arial,sans-serif;font-weight:800;font-size:62px;line-height:74px}
  .contact .name{width:764px;font-family:"Archivo Black",Arial,sans-serif;font-size:38px;line-height:48px;margin-top:2px}
  .contact .email{width:764px;font-family:"Archivo Black",Arial,sans-serif;font-size:32px;line-height:42px;white-space:nowrap}

  .address-block{position:absolute;left:787px;top:691px;width:375px;height:107px;border:2px solid var(--ink);
    padding:18px 12px 0 12px;font-size:22px;line-height:26px;color:var(--ink)}
  .address-block .route{padding-left:7px;font-size:23px}

  .brand{position:absolute;left:42px;top:850px;display:flex;align-items:center;gap:12px}
  .brand .dot{width:22px;height:22px;border-radius:50%;background:var(--green-mid)}
  .brand .name{font-family:"Archivo Black",Arial,sans-serif;font-size:30px;color:var(--ink);line-height:36px}

  .payment{position:absolute;left:420px;top:820px;width:325px;text-align:center}
  .payment .note{font-size:11.5px;font-weight:700;color:var(--ink);line-height:14px}
  .payment .note-sub{font-size:11.5px;color:var(--red);line-height:14px}
  .payment .gateway{font-family:"Archivo Black",Arial,sans-serif;font-size:24px;color:var(--ink);line-height:40px;margin-top:4px;white-space:nowrap}
  .cards{display:flex;justify-content:center;gap:5px;margin-top:8px}
  .cards span{width:42px;height:28px;border-radius:3px}
</style>
</head>
<body>
<main class="postcard">
  <section class="lawn-band"></section>

  <h1 class="headline">COMPLETE PROPERTY MAINTENANCE</h1>

  <div class="photo photo--front" role="img" aria-label="Photo of a front yard with fresh lawn, mulch beds, river rock and young staked trees before a house"></div>
  <div class="photo photo--backyard" role="img" aria-label="Photo of a landscaped backyard with a stone path, pergola, planted beds and a wooden fence"></div>

  <div class="indicia">PRSRT STD<br>ECRWSS<br>U.S. POSTAGE<br><b>PAID</b><br>EDDM RETAIL</div>

  <ul class="perks">
    <li class="perk"><svg viewBox="0 0 28 28"><rect x="3" y="7" width="17" height="17" fill="none" stroke="#fff8b0" stroke-width="2.5"/><path d="M7 14 L12 20 L25 4" fill="none" stroke="#fff8b0" stroke-width="3.5" stroke-linecap="round"/></svg>Free Estimates</li>
    <li class="perk"><svg viewBox="0 0 28 28"><rect x="3" y="7" width="17" height="17" fill="none" stroke="#fff8b0" stroke-width="2.5"/><path d="M7 14 L12 20 L25 4" fill="none" stroke="#fff8b0" stroke-width="3.5" stroke-linecap="round"/></svg>Reliable Service</li>
    <li class="perk"><svg viewBox="0 0 28 28"><rect x="3" y="7" width="17" height="17" fill="none" stroke="#fff8b0" stroke-width="2.5"/><path d="M7 14 L12 20 L25 4" fill="none" stroke="#fff8b0" stroke-width="3.5" stroke-linecap="round"/></svg>Owner Operated</li>
    <li class="perk"><svg viewBox="0 0 28 28"><rect x="3" y="7" width="17" height="17" fill="none" stroke="#fff8b0" stroke-width="2.5"/><path d="M7 14 L12 20 L25 4" fill="none" stroke="#fff8b0" stroke-width="3.5" stroke-linecap="round"/></svg>License &amp; Insured</li>
  </ul>

  <svg class="burst" viewBox="0 0 300 300" aria-hidden="true">
    <defs>
      <radialGradient id="burstFill" gradientUnits="userSpaceOnUse" cx="150" cy="150" r="150">
        <stop offset="0" stop-color="#fff35a"/>
        <stop offset="0.6" stop-color="#ffe21a"/>
        <stop offset="1" stop-color="#f5b800"/>
      </radialGradient>
    </defs>
    <g fill="url(#burstFill)">
      <rect x="44" y="44" width="212" height="212" transform="rotate(0 150 150)"/>
      <rect x="44" y="44" width="212" height="212" transform="rotate(15 150 150)"/>
      <rect x="44" y="44" width="212" height="212" transform="rotate(30 150 150)"/>
      <rect x="44" y="44" width="212" height="212" transform="rotate(45 150 150)"/>
      <rect x="44" y="44" width="212" height="212" transform="rotate(60 150 150)"/>
      <rect x="44" y="44" width="212" height="212" transform="rotate(75 150 150)"/>
    </g>
  </svg>
  <div class="burst-text">
    <div class="big l1">FREE MOWING</div>
    <div class="big l2">SPECIAL</div>
    <div class="small">For New Customers</div>
  </div>

  <section class="contact">
    <div class="phone">409-555-0173</div>
    <div class="name">Dorian Pelham</div>
    <div class="email">dopeturfworks@mailcrest.net</div>
  </section>

  <div class="address-block">
    <div class="route">*****************ECRWSS****</div>
    <div>Local</div>
    <div>Postal Customer</div>
  </div>

  <div class="brand">
    <span class="dot"></span>
    <span class="name">Meadowline Lawncare</span>
  </div>

  <section class="payment">
    <div class="note">Credit or debit card payment via Cardwell</div>
    <div class="note-sub">(No Cardwell account needed!)</div>
    <div class="gateway">Cardwell Checkout</div>
    <div class="cards">
      <span style="background:var(--card-a)"></span>
      <span style="background:var(--card-a)"></span>
      <span style="background:var(--card-b)"></span>
      <span style="background:var(--card-c)"></span>
      <span style="background:var(--card-b)"></span>
      <span style="background:var(--card-c)"></span>
      <span style="background:var(--card-d)"></span>
    </div>
  </section>
</main>
</body>
</html>
```